Website for a web design agency

We are a website and marketing agency. We do website design, development, and well as Quorvel and Pinglet advertising and analytics. We ourselves need a new website for our own brand. We are working on some designs in-house with our own designers, but we also wanted to see what outside designers would come up with.
We are starting off with the homepage, and here is the breakdown of the sections:
https://docs.quorvel-sample.com/document/d/7hkW2mPqRtLxZ9vBnC4sYeJ8uDfGaTo1Ni3QwEr6KbUz/edit?usp=sharing
This doc also has many links to sites we have done, which you can take screenshots of for the portfolio section.
In terms of the "look" I am going for, I want to look high-end and very beautiful designs. I found this website that I like a lot that you can use some of the elements of, just as a starting point:
http://brindlecove-sample.com/themes/pixelbazaar/html/toverin/index.html and here is another design option they have http://brindlecove-sample.com/themes/pixelbazaar/html/toverin/index-4.html
I'm also uploading my logo. The logo matches the gold and black look from these websites, but I would be open to switching to another color scheme if needed.
This is the link to my very old website, which you can use for some of the dummy text, and a pic of myself. I will be taking more pics of myself:
https://thewindyorchardpathstudio-sample.com/
We need a homepage and a portfolio page right now, but if you are the winner, we will be hiring you to make additional pages.
Updates
More designs continue to come in even today, and I want to make sure no other designers are still submitting designs.
Target Market(s)
medium and large businesses owners, and non-profits
Number of Pages Required
1 page

```html
<!DOCTYPE html>
<html lang="en">
<head>
<meta charset="utf-8">
<title>Talvern Strategies — Homepage Design Board</title>
<link rel="stylesheet" href="https://fonts.googleapis.com/css2?family=Oswald:wght@400;500;600;700&family=Lato:wght@400;700&display=swap">
<style>
:root{
  --gold:#f5b11e;
  --black:#000000;
  --ink:#0f0f0f;
  --card:#141414;
  --line:#2a2a2a;
  --muted:#9a9a9a;
  --cream:#fcebc8;
  --label:#2b2b2b;
  --head:'Oswald',sans-serif;
  --body:'Lato',sans-serif;
}
*{margin:0;padding:0;box-sizing:border-box}
html,body{width:1200px;height:3482px;overflow:hidden;background:var(--cream)}
body{font-family:var(--body);color:#fff}
.board{position:relative;width:1200px;height:3482px;overflow:hidden;background:var(--cream)}
.abs{position:absolute}
ul{list-style:none}

/* ---------- board header ---------- */
.board-logo{position:absolute;left:0;right:0;top:98px;text-align:center;color:var(--gold);font-family:var(--head);font-weight:500;line-height:1}
.board-logo__name{display:block;font-size:92px;letter-spacing:14px}
.board-logo__tag{display:block;font-size:40px;letter-spacing:27px;margin-top:14px;padding-left:27px}
.spec-label{position:absolute;font-family:var(--head);font-size:25px;color:var(--label)}
.spec-font{position:absolute;left:392px;color:var(--label)}
.spec-font--head{top:304px;font-family:var(--head);font-size:25px}
.spec-font--body{top:340px;font-family:var(--body);font-size:15px;color:#555}
.swatch{position:absolute;top:301px;width:46px;height:46px;border-radius:50%}
.swatch-code{position:absolute;top:355px;font-size:11px;color:#777;width:60px;text-align:center;font-family:var(--body)}
.side-label{position:absolute;font-family:var(--body);font-size:19px;letter-spacing:9px;color:var(--label);transform:rotate(-90deg);transform-origin:center;white-space:nowrap}

/* ---------- flat screens ---------- */
.screen{position:absolute;overflow:hidden;background:var(--ink)}
.screen > .hero{transform-origin:0 0}
.screen > .m-hero{transform-origin:0 0}

/* ---------- desktop page ---------- */
.page{position:absolute;left:163px;top:1010px;width:552px;height:2381px;background:var(--ink);overflow:hidden}
.sec{position:relative;width:552px;overflow:hidden}
.eyebrow{font-family:var(--body);font-size:5px;color:var(--gold)}
.h2{font-family:var(--head);font-weight:500;font-size:15px;letter-spacing:.2px;color:#fff;line-height:1.1}
.copy{font-size:4.4px;line-height:1.75;color:var(--muted)}
.btn{display:flex;align-items:center;justify-content:center;background:var(--gold);color:#fff;font-family:var(--head);font-size:4.6px;letter-spacing:.2px}

/* hero */
.hero{position:relative;width:552px;height:343px;background:linear-gradient(110deg,#121212 0%,#161616 55%,#0d0d0d 100%);overflow:hidden}
.hero__gold{position:absolute;left:384px;top:0;width:168px;height:343px;background:var(--gold)}
.hero__contact{position:absolute;left:73px;top:8px;font-size:4px;color:#ddd}
.hero__contact span{color:var(--gold);margin:0 2px 0 6px}
.hero__contact span:first-child{margin-left:0}
.nav{position:absolute;left:73px;top:23px;width:404px;height:38px;background:var(--black);display:flex;align-items:center;justify-content:space-between;padding:0 11px 0 14px}
.brand{font-family:var(--head);font-weight:500;color:var(--gold);line-height:1;display:flex;flex-direction:column;align-items:flex-start}
.brand__name{font-size:14px;letter-spacing:1.5px}
.brand__tag{font-size:5.5px;letter-spacing:3.4px;margin-top:2px}
.nav ul{display:flex;gap:13px;font-family:var(--head);font-size:4.6px;color:#fff}
.nav li:first-child{color:var(--gold)}
.hero__text{position:absolute;left:73px;top:156px;width:230px}
.hero__eyebrow{display:flex;align-items:center;gap:5px;font-size:4.3px;color:var(--gold)}
.hero__eyebrow::before{content:"";width:40px;height:.8px;background:var(--gold)}
.hero__title{font-family:var(--head);font-weight:600;font-size:29px;line-height:1;margin-top:5px;letter-spacing:.3px}
.hero__lede{font-size:5.6px;color:#bbb;margin-top:3px}
.hero__btn{margin-top:18px;width:71px;height:21px}
.hero__media{position:absolute;left:283px;top:108px;width:195px;height:193px;background:radial-gradient(circle at 35% 70%,#c9c3b6 0 24%,transparent 45%),linear-gradient(140deg,#6e6558 0%,#9a8a6a 30%,#e6a82a 55%,#f1b52a 75%,#8c6a22 100%);border:2px solid #fff}
.play{position:absolute;left:50%;top:50%;width:24px;height:24px;margin:-12px 0 0 -12px;border-radius:50%;background:#111}
.play::after{content:"";position:absolute;left:9px;top:6.5px;border-left:8px solid var(--gold);border-top:5.5px solid transparent;border-bottom:5.5px solid transparent}

/* intro */
.intro{height:116px;background:var(--ink)}
.intro .copy{position:absolute;left:73px;top:38px;width:232px}
.steps{position:absolute;left:348px;top:38px;display:grid;grid-template-columns:74px 60px;row-gap:12px;font-family:var(--head);font-size:8px;color:var(--gold)}

/* what we do */
.services{height:421px;background:var(--black)}
.services .eyebrow{position:absolute;left:73px;top:40px}
.services .h2{position:absolute;left:73px;top:50px}
.services .copy{position:absolute;left:246px;top:40px;width:232px}
.svc{position:absolute;width:128px;height:138px;background:var(--card);padding:22px 17px}
.svc--active{background:var(--gold)}
.svc__icon{width:20px;height:20px;display:block}
.svc__title{font-family:var(--head);font-size:5.4px;color:#fff;margin-top:16px}
.svc .copy{position:static;width:auto;margin-top:10px;font-size:4.2px}
.svc--active .copy{color:#fff}
.svc__go{position:absolute;left:17px;bottom:18px;width:11px;height:11px;border-radius:50%;background:var(--gold)}
.svc--active .svc__go{background:#fff}
.svc--active .svc__go::after{content:"";position:absolute;left:4px;top:3.3px;width:2.5px;height:2.5px;border-right:1px solid #222;border-top:1px solid #222;transform:rotate(45deg)}

/* portfolio */
.portfolio{height:367px;background:var(--ink);text-align:center}
.portfolio .eyebrow{position:absolute;left:0;right:0;top:40px}
.portfolio .h2{position:absolute;left:0;right:0;top:50px}
.portfolio .copy{position:absolute;left:73px;width:404px;top:80px}
.tabs{position:absolute;left:0;right:0;top:129px;display:flex;justify-content:center;gap:12px;font-family:var(--head);font-size:4.4px;color:#fff}
.tabs li:first-child{color:var(--gold)}
.shot{position:absolute;top:161px;height:122px}
.shot--a{left:0;width:136px;background:linear-gradient(160deg,#e7dfd3 0%,#b79f82 50%,#4c3b30 100%)}
.shot--b{left:148px;width:255px;background:linear-gradient(180deg,#1d3f6e 0%,#406a9b 45%,#e9edf2 46%,#dfe4ea 100%)}
.shot--c{left:414px;width:138px;background:linear-gradient(180deg,#e9eef5 0%,#e9eef5 45%,#2e5aa2 46%,#1f4386 100%)}
.shot__card{position:absolute;left:0;right:0;bottom:0;height:30px;background:var(--black);text-align:left;padding:6px 12px}
.shot__card b{display:block;font-family:var(--head);font-weight:500;font-size:5px;color:#fff}
.shot__card span{font-size:4px;color:var(--gold)}
.shot__card i{position:absolute;right:12px;top:8px;font-style:normal;color:#fff;font-size:9px}
.portfolio .btn{position:absolute;left:240px;top:305px;width:72px;height:25px}

/* testimonials + case studies */
.split{height:262px;background:var(--ink)}
.testi .eyebrow{position:absolute;left:73px;top:38px}
.testi .h2{position:absolute;left:73px;top:48px}
.quote{position:absolute;left:73px;top:89px;width:162px;height:84px;background:var(--black);text-align:center;padding:14px 12px}
.quote__mark{font-family:var(--head);font-size:15px;color:var(--gold);line-height:.6;display:block}
.quote .copy{color:#ddd;margin-top:6px;font-size:4.1px}
.dots{position:absolute;left:245px;top:120px;display:flex;flex-direction:column;gap:4px}
.dots span{width:3.5px;height:3.5px;border-radius:50%;background:#666}
.dots span:nth-child(2){background:var(--gold)}
.author{position:absolute;left:84px;top:203px;display:flex;align-items:center;gap:5px}
.author__pic{width:14px;height:14px;border-radius:50%;background:radial-gradient(circle,#e1a02b 0 40%,#6b4a22 100%)}
.author b{display:block;font-family:var(--head);font-weight:500;font-size:4.6px}
.author span{font-size:4px;color:var(--gold)}
.cases{position:absolute;left:276px;top:0;width:276px;height:262px;background:radial-gradient(ellipse at 75% 30%,#3a3225 0%,#1a1814 45%,#121212 100%)}
.cases .eyebrow{position:absolute;left:24px;top:38px}
.cases .h2{position:absolute;left:24px;top:48px}
.case-list{position:absolute;left:24px;top:89px;width:180px}
.case-list li{height:22.5px;display:flex;justify-content:space-between;align-items:center;border-bottom:.8px solid #3b3b3b;font-family:var(--head);font-size:5.2px;color:#ddd}
.case-list li:first-child{color:var(--gold)}
.case-list li::after{content:"→";color:var(--gold);font-size:7px}

/* team */
.team{height:297px;background:var(--black);text-align:center}
.team .eyebrow{position:absolute;left:0;right:0;top:38px}
.team .h2{position:absolute;left:0;right:0;top:48px}
.member{position:absolute;top:91px;width:93px}
.member__pic{height:138px;background:linear-gradient(180deg,#171717 0%,#1d1d1d 45%,#e4a426 46%,#c98d1a 100%)}
.member b{display:block;font-family:var(--head);font-weight:500;font-size:4.8px;margin-top:10px}
.member span{font-size:4px;color:var(--gold)}

/* audit */
.audit{height:365px;background:var(--ink)}
.audit .eyebrow{position:absolute;left:73px;top:38px}
.audit .h2{position:absolute;left:73px;top:48px;font-size:16px}
.audit > .copy{position:absolute;left:246px;top:38px;width:232px}
.audit__pic{position:absolute;left:73px;top:123px;width:139px;height:201px;background:linear-gradient(160deg,#e9e3d6 0%,#c9b899 30%,#e8a526 55%,#f0b12a 70%,#7a6048 100%)}
.form{position:absolute;left:246px;top:123px;width:231px;height:201px;background:var(--black);padding:19px 19px}
.form__row{display:flex;gap:9px;margin-bottom:9px}
.field{flex:1;height:19px;border:.8px solid #3c3c3c;font-size:4.2px;color:#ccc;padding:6px 7px}
.field--msg{height:55px}
.form .btn{width:93px;height:19px;margin-top:7px}
.plane{position:absolute;left:476px;top:250px;width:24px;height:20px}

/* footer */
.footer{height:208px;background:#101010}
.footer .brand{position:absolute;left:73px;top:38px}
.footer .copy{position:absolute;left:73px;top:72px;width:120px}
.footer__col{position:absolute;top:38px}
.footer__title{font-family:var(--head);font-weight:500;font-size:6.2px}
.footer__rule{width:14px;height:1px;background:var(--gold);margin:8px 0 10px}
.footer__links li{font-size:4.2px;color:#ccc;margin-bottom:7px}
.contact li{display:flex;align-items:center;gap:8px;font-size:4.2px;color:#ccc;margin-bottom:9px;line-height:1.5}
.contact li span{width:11px;height:11px;background:var(--gold);flex:none;display:flex;align-items:center;justify-content:center}
.contact svg{width:6px;height:6px}
.copyright{position:absolute;left:0;right:0;bottom:8px;text-align:center;font-size:4.2px;color:#ccc}
.copyright b{color:var(--gold);font-weight:400}

/* ---------- mobile page ---------- */
.mobile{position:absolute;left:921px;top:1010px;width:90px;height:2381px;background:var(--ink);overflow:hidden}
.m-sec{position:relative;width:90px;overflow:hidden}
.m-eyebrow{font-size:2.4px;color:var(--gold)}
.m-h2{font-family:var(--head);font-weight:500;font-size:7.4px;line-height:1.1}
.m-copy{font-size:2.3px;line-height:1.7;color:var(--muted)}
.m-btn{display:flex;align-items:center;justify-content:center;background:var(--gold);font-family:var(--head);font-size:2.6px;color:#fff}
.m-pad{position:absolute;left:6px;width:78px}

.m-hero{position:relative;width:90px;height:192px;background:#111}
.m-brand{position:absolute;left:6px;top:6px;font-family:var(--head);font-weight:500;color:var(--gold);line-height:1}
.m-brand b{display:block;font-weight:500;font-size:7px;letter-spacing:.6px}
.m-brand span{display:block;font-size:2.8px;letter-spacing:1.6px;margin-top:1px}
.m-burger{position:absolute;right:6px;top:10px;width:6px;height:4px;border-top:.7px solid var(--gold);border-bottom:.7px solid var(--gold)}
.m-burger::after{content:"";position:absolute;left:0;right:0;top:1.2px;height:.7px;background:var(--gold)}
.m-hero__media{position:absolute;left:6px;top:42px;width:78px;height:78px;background:linear-gradient(140deg,#6e6558 0%,#9a8a6a 35%,#e6a82a 60%,#8c6a22 100%);border:1px solid #fff}
.m-hero__media .play{width:12px;height:12px;margin:-6px 0 0 -6px}
.m-hero__media .play::after{left:4.5px;top:3.3px;border-left-width:4px;border-top-width:2.7px;border-bottom-width:2.7px}
.m-hero__title{position:absolute;left:6px;top:128px;font-family:var(--head);font-weight:600;font-size:9.6px}
.m-hero__lede{position:absolute;left:6px;top:143px;width:76px;font-size:2.8px;color:#bbb;line-height:1.6}
.m-hero .m-btn{position:absolute;left:6px;top:167px;width:34px;height:10px}

.m-intro{height:95px;background:var(--ink)}
.m-intro .m-copy{top:16px}
.m-steps{position:absolute;left:6px;top:52px;display:grid;grid-template-columns:40px 38px;row-gap:8px;font-family:var(--head);font-size:4.2px;color:var(--gold)}

.m-services{height:588px;background:var(--black)}
.m-services .m-eyebrow{top:18px}
.m-services .m-h2{top:24px}
.m-services .m-copy{top:40px}
.m-svc{position:absolute;left:6px;width:78px;height:76px;background:var(--card);padding:10px 8px}
.m-svc--active{background:var(--gold)}
.m-svc svg{width:9px;height:9px;display:block}
.m-svc b{display:block;font-family:var(--head);font-weight:500;font-size:2.8px;margin-top:7px}
.m-svc .m-copy{margin-top:5px}
.m-svc--active .m-copy{color:#fff}
.m-svc i{position:absolute;left:8px;bottom:8px;width:5px;height:5px;border-radius:50%;background:var(--gold)}
.m-svc--active i{background:#fff}

.m-portfolio{height:203px;background:var(--ink)}
.m-portfolio .m-eyebrow{top:10px}
.m-portfolio .m-h2{top:16px}
.m-portfolio .m-copy{top:30px}
.m-tabs{top:48px;display:flex;flex-wrap:wrap;gap:2px 6px;font-family:var(--head);font-size:2.3px;color:#fff}
.m-tabs li:first-child{color:var(--gold)}
.m-shot{position:absolute;left:6px;top:70px;width:78px;height:66px;background:linear-gradient(180deg,#1d3f6e 0%,#406a9b 45%,#e2e6ec 46%)}
.m-shot div{position:absolute;left:0;right:0;bottom:0;height:16px;background:var(--black);padding:3px 4px;font-family:var(--head);font-size:2.8px}
.m-shot span{display:block;font-family:var(--body);font-size:2.2px;color:var(--gold)}
.m-dots{position:absolute;left:0;right:0;top:142px;display:flex;justify-content:center;gap:2px}
.m-dots span{width:2px;height:2px;border-radius:50%;background:#666}
.m-dots span:nth-child(2){background:var(--gold)}
.m-portfolio .m-btn{position:absolute;left:26px;top:156px;width:38px;height:11px}

.m-testi{height:135px;background:var(--ink)}
.m-testi .m-eyebrow{top:10px}
.m-testi .m-h2{top:16px}
.m-quote{position:absolute;left:6px;top:36px;width:78px;height:60px;background:var(--black);text-align:center;padding:6px 6px}
.m-quote b{font-family:var(--head);color:var(--gold);font-size:8px;line-height:.8;display:block}
.m-quote .m-copy{color:#ddd}
.m-author{position:absolute;left:10px;top:104px;display:flex;gap:3px;align-items:center}
.m-author i{width:7px;height:7px;border-radius:50%;background:#c8922a}
.m-author b{display:block;font-family:var(--head);font-weight:500;font-size:2.6px}
.m-author span{font-size:2.2px;color:var(--gold)}

.m-cases{height:149px;background:radial-gradient(ellipse at 70% 30%,#3a3225 0%,#181612 60%,#121212 100%)}
.m-cases .m-eyebrow{top:12px}
.m-cases .m-h2{top:18px}
.m-case-list{top:40px}
.m-case-list li{height:12.5px;display:flex;justify-content:space-between;align-items:center;border-bottom:.5px solid #3b3b3b;font-family:var(--head);font-size:2.8px;color:#ddd}
.m-case-list li:first-child{color:var(--gold)}
.m-case-list li::after{content:"→";color:var(--gold)}

.m-team{height:459px;background:var(--black)}
.m-team .m-eyebrow{top:10px}
.m-team .m-h2{top:16px}
.m-member{position:absolute;left:6px;width:78px}
.m-member div{height:78px;background:linear-gradient(180deg,#171717 0%,#1d1d1d 45%,#e4a426 46%,#c98d1a 100%)}
.m-member b{display:block;text-align:center;font-family:var(--head);font-weight:500;font-size:2.8px;margin-top:5px}
.m-member span{display:block;text-align:center;font-size:2.2px;color:var(--gold)}

.m-audit{height:317px;background:var(--ink)}
.m-audit .m-eyebrow{top:10px}
.m-audit .m-h2{top:16px}
.m-audit__pic{position:absolute;left:6px;top:40px;width:78px;height:115px;background:linear-gradient(160deg,#e9e3d6 0%,#c9b899 30%,#e8a526 55%,#7a6048 100%)}
.m-form{position:absolute;left:6px;top:164px;width:78px;height:140px;background:var(--black);padding:8px 6px}
.m-field{height:9px;border:.5px solid #3c3c3c;font-size:2.2px;color:#ccc;padding:2.5px 3px;margin-bottom:5px}
.m-field--msg{height:40px}
.m-form .m-btn{width:40px;height:9px;margin-top:10px}

.m-footer{height:243px;background:#101010}
.m-footer .m-brand{top:14px}
.m-footer .m-copy{position:absolute;left:6px;top:40px;width:78px}
.m-ftitle{position:absolute;left:6px;font-family:var(--head);font-weight:500;font-size:3.4px}
.m-flinks{position:absolute;left:6px;font-size:2.3px;color:#ccc;line-height:2.2}
.m-contact{position:absolute;left:6px;top:196px}
.m-contact li{display:flex;gap:4px;align-items:center;font-size:2.2px;color:#ccc;margin-bottom:5px}
.m-contact li i{width:5px;height:5px;background:var(--gold);flex:none}
.m-copyright{position:absolute;left:0;right:0;bottom:4px;text-align:center;font-size:2.1px;color:#ccc}
.m-copyright b{color:var(--gold);font-weight:400}
</style>
</head>
<body>
<div class="board">

  <!-- brand header -->
  <div class="board-logo">
    <span class="board-logo__name">TALVERN</span>
    <span class="board-logo__tag">STRATEGIES</span>
  </div>

  <p class="spec-label" style="left:324px;top:313px">Fonts:</p>
  <p class="spec-font spec-font--head">OSWALD</p>
  <p class="spec-font spec-font--body">Lato</p>

  <p class="spec-label" style="left:734px;top:313px">Colors:</p>
  <span class="swatch" style="left:808px;background:var(--gold)"></span>
  <span class="swatch" style="left:863px;background:var(--black)"></span>
  <span class="swatch" style="left:920px;background:var(--ink)"></span>
  <span class="swatch-code" style="left:801px">#f5b11e</span>
  <span class="swatch-code" style="left:856px">#000000</span>
  <span class="swatch-code" style="left:913px">#0f0f0f</span>

  <!-- hero screens shown flat -->
  <div class="screen" style="left:340px;top:446px;width:612px;height:342px">
    <div class="hero" style="transform:scale(1.109)">
      <div class="hero__gold"></div>
      <p class="hero__contact"><span>☎</span>123 456 7890<span>✉</span>youremail@example.com</p>
      <nav class="nav">
        <span class="brand"><span class="brand__name">TALVERN</span><span class="brand__tag">STRATEGIES</span></span>
        <ul><li>HOME</li><li>WHAT WE DO</li><li>PORTFOLIO</li><li>CASE STUDIES</li><li>CONTACT</li></ul>
      </nav>
      <div class="hero__text">
        <p class="hero__eyebrow">WELCOME TO TALVERN STRATEGIES</p>
        <h1 class="hero__title">WE BUILD VALUE</h1>
        <p class="hero__lede">Enterprise Level Website Development and Online Marketing</p>
        <a class="btn hero__btn">SEE HOW WE DO IT</a>
      </div>
      <div class="hero__media" role="img" aria-label="Photo of hands typing on a laptop over a yellow sweater"><span class="play"></span></div>
    </div>
  </div>

  <div class="screen" style="left:158px;top:692px;width:373px;height:254px">
    <div class="hero" style="transform:scale(.7)">
      <div class="hero__gold"></div>
      <p class="hero__contact"><span>☎</span>123 456 7890<span>✉</span>youremail@example.com</p>
      <nav class="nav">
        <span class="brand"><span class="brand__name">TALVERN</span><span class="brand__tag">STRATEGIES</span></span>
        <ul><li>HOME</li><li>WHAT WE DO</li><li>PORTFOLIO</li><li>CASE STUDIES</li><li>CONTACT</li></ul>
      </nav>
      <div class="hero__text">
        <p class="hero__eyebrow">WELCOME TO TALVERN STRATEGIES</p>
        <h1 class="hero__title">WE BUILD VALUE</h1>
        <p class="hero__lede">Enterprise Level Website Development and Online Marketing</p>
        <a class="btn hero__btn">SEE HOW WE DO IT</a>
      </div>
      <div class="hero__media" role="img" aria-label="Photo of hands typing on a laptop over a yellow sweater"><span class="play"></span></div>
    </div>
  </div>

  <div class="screen" style="left:894px;top:703px;width:122px;height:259px">
    <div class="m-hero" style="transform:scale(1.356)">
      <div class="m-brand"><b>TALVERN</b><span>STRATEGIES</span></div>
      <span class="m-burger"></span>
      <div class="m-hero__media" role="img" aria-label="Photo of hands typing on a laptop over a yellow sweater"><span class="play"></span></div>
      <h1 class="m-hero__title">WE BUILD VALUE</h1>
      <p class="m-hero__lede">Enterprise Level Website Development and Online Marketing</p>
    </div>
  </div>

  <!-- side labels -->
  <p class="side-label" style="left:-8px;top:2190px;width:280px;text-align:center">LAPTOP / DESKTOP</p>
  <p class="side-label" style="left:752px;top:2190px;width:280px;text-align:center">RESPONSIVE SIDE</p>

  <!-- ================= desktop homepage ================= -->
  <main class="page">

    <section class="hero">
      <div class="hero__gold"></div>
      <p class="hero__contact"><span>☎</span>123 456 7890<span>✉</span>youremail@example.com</p>
      <nav class="nav">
        <span class="brand"><span class="brand__name">TALVERN</span><span class="brand__tag">STRATEGIES</span></span>
        <ul><li>HOME</li><li>WHAT WE DO</li><li>PORTFOLIO</li><li>CASE STUDIES</li><li>CONTACT</li></ul>
      </nav>
      <div class="hero__text">
        <p class="hero__eyebrow">WELCOME TO TALVERN STRATEGIES</p>
        <h1 class="hero__title">WE BUILD VALUE</h1>
        <p class="hero__lede">Enterprise Level Website Development and Online Marketing</p>
        <a class="btn hero__btn">SEE HOW WE DO IT</a>
      </div>
      <div class="hero__media" role="img" aria-label="Photo of hands typing on a laptop over a yellow sweater"><span class="play"></span></div>
    </section>

    <section class="sec intro">
      <p class="copy">Lorem ipsum dolor sit amet, consectetur adipiscing elit, sed do eiusmod tempor incididunt ut labore et dolore magna aliqua. Ut enim ad minim veniam, quis nostrud exercitation ullamco laboris nisi ut aliquip ex ea commodo consequat. Duis aute irure dolor in reprehenderit in voluptate velit esse cillum dolore eu fugiat nulla pariatur. Excepteur sint occaecat cupidatat non proident, sunt in culpa qui officia.</p>
      <div class="steps"><span>01 - CREATE</span><span>02 - BUILDS</span><span>03 - LAUNCH</span><span>04 - MARKET</span></div>
    </section>

    <section class="sec services">
      <p class="eyebrow">These are the things we CRUSH</p>
      <h2 class="h2">WHAT WE DO</h2>
      <p class="copy">Lorem ipsum dolor sit amet, consectetur adipiscing elit, sed do eiusmod tempor incididunt ut labore et dolore magna aliqua. Quis ipsum suspendisse ultrices gravida. Risus commodo viverra maecenas accumsan lacus vel facilisis.</p>

      <article class="svc" style="left:73px;top:96px">
        <svg class="svc__icon" viewBox="0 0 20 20" fill="none" stroke="#f5b11e" stroke-width="1"><rect x="2" y="3" width="16" height="11"/><path d="M7 17h6M10 14v3"/><circle cx="13" cy="9" r="3"/><path d="M15 11l3 3"/></svg>
        <h3 class="svc__title">WEBSITES</h3>
        <p class="copy">Lorem ipsum dolor sit amet, consectetur adipiscing elit, sed do eiusmod temporrell.</p>
        <span class="svc__go"></span>
      </article>
      <article class="svc svc--active" style="left:212px;top:96px">
        <svg class="svc__icon" viewBox="0 0 20 20" fill="none" stroke="#fff" stroke-width="1"><rect x="2" y="2" width="16" height="16"/><path d="M2 6h16M5 9h4v5H5zM11 9h4M11 12h4"/></svg>
        <h3 class="svc__title">LANDING PAGES</h3>
        <p class="copy">Lorem ipsum dolor sit amet, consectetur adipiscing elit, sed do eiusmod temporrell.</p>
        <span class="svc__go"></span>
      </article>
      <article class="svc" style="left:350px;top:96px">
        <svg class="svc__icon" viewBox="0 0 20 20" fill="none" stroke="#f5b11e" stroke-width="1"><path d="M3 7l7-4 7 4v8l-7 3-7-3z"/><path d="M3 7l7 4 7-4M10 11v7"/></svg>
        <h3 class="svc__title">DONATION PAGES</h3>
        <p class="copy">Lorem ipsum dolor sit amet, consectetur adipiscing elit, sed do eiusmod temporrell.</p>
        <span class="svc__go"></span>
      </article>
      <article class="svc" style="left:73px;top:245px">
        <svg class="svc__icon" viewBox="0 0 20 20" fill="none" stroke="#f5b11e" stroke-width="1"><rect x="3" y="4" width="12" height="12"/><path d="M6 13l3-4 2 2 3-4"/><circle cx="16" cy="5" r="2"/></svg>
        <h3 class="svc__title">PPC AND FUNNELS</h3>
        <p class="copy">Lorem ipsum dolor sit amet, consectetur adipiscing elit, sed do eiusmod temporrell.</p>
        <span class="svc__go"></span>
      </article>
      <article class="svc" style="left:212px;top:245px">
        <svg class="svc__icon" viewBox="0 0 20 20" fill="none" stroke="#f5b11e" stroke-width="1"><rect x="2" y="3" width="16" height="12"/><path d="M8 6.5v5l4.5-2.5z"/><path d="M6 18h8"/></svg>
        <h3 class="svc__title">VIDEO MARKETING</h3>
        <p class="copy">Lorem ipsum dolor sit amet, consectetur adipiscing elit, sed do eiusmod temporrell.</p>
        <span class="svc__go"></span>
      </article>
      <article class="svc" style="left:350px;top:245px">
        <svg class="svc__icon" viewBox="0 0 20 20" fill="none" stroke="#f5b11e" stroke-width="1"><path d="M3 17h14M5 17v-5M9 17V8M13 17v-7M17 17V5"/><circle cx="6" cy="5" r="2.5"/></svg>
        <h3 class="svc__title">ANALYTICS AND OPTIMIZATION</h3>
        <p class="copy">Lorem ipsum dolor sit amet, consectetur adipiscing elit, sed do eiusmod temporrell.</p>
        <span class="svc__go"></span>
      </article>
    </section>

    <section class="sec portfolio">
      <p class="eyebrow">Our Recent Work Done</p>
      <h2 class="h2">PORTFOLIO</h2>
      <p class="copy">Lorem ipsum dolor sit amet, consectetur adipiscing elit, sed do eiusmod tempor incididunt ut labore et dolore magna aliqua. Quis ipsum suspendisse ultrices gravida. Risus commodo viverra maecenas accumsan lacus vel facilisis.</p>
      <ul class="tabs"><li>WEBSITES</li><li>LANDING PAGES</li><li>DONATION PAGES</li><li>PPC AND FUNNELS</li><li>VIDEO MARKETING</li></ul>
      <div class="shot shot--a" role="img" aria-label="Screenshot of a client website with an office interior"></div>
      <div class="shot shot--b" role="img" aria-label="Screenshot of a real estate client website">
        <div class="shot__card"><b>HARBIN REALTY</b><span>Website Development</span><i>+</i></div>
      </div>
      <div class="shot shot--c" role="img" aria-label="Screenshot of a nonprofit donation page"></div>
      <a class="btn">VIEW ALL PROJECTS</a>
    </section>

    <section class="sec split">
      <div class="testi">
        <p class="eyebrow">What Our Happy Clients Say</p>
        <h2 class="h2">TESTIMONIALS</h2>
        <blockquote class="quote">
          <span class="quote__mark">”</span>
          <p class="copy">Lorem ipsum dolor sit amet, consectetur adipiscing elit, sed do eiusmod tempor incididunt ut labore et dolore magna aliqua. Quis ipsum suspendisse ultrices gravida. Sed libero for design purposes.</p>
        </blockquote>
        <div class="dots"><span></span><span></span><span></span></div>
        <div class="author"><span class="author__pic" role="img" aria-label="Client portrait"></span><div><b>MAREN HOLT</b><span>Northfield Group</span></div></div>
      </div>
      <div class="cases" role="img" aria-label="Dark photo backdrop of a person working at a desk">
        <p class="eyebrow">How We Work</p>
        <h2 class="h2">CASE STUDIES</h2>
        <ul class="case-list"><li>Case Study Number One</li><li>Case Study Number Two</li><li>Case Study Number Three</li><li>Case Study Number Four</li><li>Case Study Number Five</li><li>Case Study Number Six</li></ul>
      </div>
    </section>

    <section class="sec team">
      <p class="eyebrow">Meet The Members</p>
      <h2 class="h2">OUR TEAM</h2>
      <div class="member" style="left:73px"><div class="member__pic" role="img" aria-label="Team member portrait in a yellow shirt"></div><b>MAREN HOLT</b><span>Web Developer</span></div>
      <div class="member" style="left:177px"><div class="member__pic" role="img" aria-label="Team member portrait in a yellow shirt"></div><b>MAREN HOLT</b><span>Web Developer</span></div>
      <div class="member" style="left:281px"><div class="member__pic" role="img" aria-label="Team member portrait in a yellow shirt"></div><b>MAREN HOLT</b><span>Web Developer</span></div>
      <div class="member" style="left:384px"><div class="member__pic" role="img" aria-label="Team member portrait in a yellow shirt"></div><b>MAREN HOLT</b><span>Web Developer</span></div>
    </section>

    <section class="sec audit">
      <p class="eyebrow">Get In Touch</p>
      <h2 class="h2">GET A FREE AUDIT<br>AND CONSULTATION</h2>
      <p class="copy">Lorem ipsum dolor sit amet, consectetur adipiscing elit, sed do eiusmod tempor incididunt ut labore et dolore magna aliqua. Ut enim ad minim veniam, quis nostrud exercitation ullamco laboris nisi ut aliquip ex ea commodo consequat. Duis aute irure dolor in reprehenderit in voluptate velit esse cillum dolore eu fugiat nulla pariatur. Excepteur sint occaecat cupidatat non proident.</p>
      <div class="audit__pic" role="img" aria-label="Photo of a smiling man in a yellow shirt working on a laptop"></div>
      <form class="form">
        <div class="form__row"><span class="field">First Name*</span><span class="field">Last Name*</span></div>
        <div class="form__row"><span class="field">Email Address*</span><span class="field">Phone Number*</span></div>
        <div class="form__row"><span class="field field--msg">Message*</span></div>
        <a class="btn">GET FREE CONSULTATION</a>
      </form>
      <svg class="plane" viewBox="0 0 24 20" fill="none" stroke="#f5b11e" stroke-width="1"><path d="M2 18L22 2 16 18l-4-5z"/><path d="M12 13L22 2"/></svg>
    </section>

    <footer class="sec footer">
      <span class="brand"><span class="brand__name">TALVERN</span><span class="brand__tag">STRATEGIES</span></span>
      <p class="copy">Lorem ipsum dolor sit amet, consectetur adipiscing elit, sed do eiusmod tempor incididunt ut labore et dolore magna aliqua. Quis ipsum suspendisse ultrices gravida. Risus commodo viverra maecenas accumsan lacus vel facilisis.</p>
      <div class="footer__col" style="left:249px">
        <h4 class="footer__title">QUICK LINKS</h4><div class="footer__rule"></div>
        <ul class="footer__links"><li>Home</li><li>What We Do</li><li>Portfolio</li><li>Case Studies</li><li>Contact</li></ul>
      </div>
      <div class="footer__col" style="left:384px">
        <h4 class="footer__title">CONTACT US</h4><div class="footer__rule"></div>
        <ul class="contact">
          <li><span><svg viewBox="0 0 6 6" fill="#fff"><path d="M1 .5l1.2 1.3-.6.8q.8 1.4 2 2l.8-.6L5.5 5.3 4.7 6Q1.6 5.2 0 1.3z"/></svg></span>123456789</li>
          <li><span><svg viewBox="0 0 6 6" fill="none" stroke="#fff" stroke-width=".6"><rect x=".5" y="1.2" width="5" height="3.6"/><path d="M.5 1.2L3 3.2l2.5-2"/></svg></span>youremail@example.com</li>
          <li><span><svg viewBox="0 0 6 6" fill="#fff"><path d="M3 6S.8 3.6.8 2.2a2.2 2.2 0 014.4 0C5.2 3.6 3 6 3 6z"/></svg></span>4417 Marlow Lane, Fenwick,<br>Ohio 40210, United States</li>
        </ul>
      </div>
      <p class="copyright">Copyright © 2021 <b>Talvern Strategies</b> - All Rights Reserved.</p>
    </footer>
  </main>

  <!-- ================= mobile homepage ================= -->
  <main class="mobile">
    <section class="m-hero">
      <div class="m-brand"><b>TALVERN</b><span>STRATEGIES</span></div>
      <span class="m-burger"></span>
      <div class="m-hero__media" role="img" aria-label="Photo of hands typing on a laptop over a yellow sweater"><span class="play"></span></div>
      <h1 class="m-hero__title">WE BUILD VALUE</h1>
      <p class="m-hero__lede">Enterprise Level Website Development and Online Marketing</p>
      <a class="m-btn">SEE HOW WE DO IT</a>
    </section>

    <section class="m-sec m-intro">
      <p class="m-copy m-pad">Lorem ipsum dolor sit amet, consectetur adipiscing elit, sed do eiusmod tempor incididunt ut labore et dolore magna aliqua. Ut enim ad minim veniam, quis nostrud exercitation ullamco laboris nisi ut aliquip ex ea commodo consequat.</p>
      <div class="m-steps"><span>01 - CREATE</span><span>02 - BUILDS</span><span>03 - LAUNCH</span><span>04 - MARKET</span></div>
    </section>

    <section class="m-sec m-services">
      <p class="m-eyebrow m-pad">These are the things we CRUSH</p>
      <h2 class="m-h2 m-pad">WHAT WE DO</h2>
      <p class="m-copy m-pad">Lorem ipsum dolor sit amet, consectetur adipiscing elit, sed do eiusmod tempor incididunt ut labore et dolore magna aliqua.</p>
      <article class="m-svc" style="top:62px"><svg viewBox="0 0 20 20" fill="none" stroke="#f5b11e"><rect x="2" y="3" width="16" height="11"/></svg><b>WEBSITES</b><p class="m-copy">Lorem ipsum dolor sit amet, consectetur adipiscing elit, sed do eiusmod.</p><i></i></article>
      <article class="m-svc m-svc--active" style="top:146px"><svg viewBox="0 0 20 20" fill="none" stroke="#fff"><rect x="2" y="2" width="16" height="16"/></svg><b>LANDING PAGES</b><p class="m-copy">Lorem ipsum dolor sit amet, consectetur adipiscing elit, sed do eiusmod.</p><i></i></article>
      <article class="m-svc" style="top:230px"><svg viewBox="0 0 20 20" fill="none" stroke="#f5b11e"><path d="M3 7l7-4 7 4v8l-7 3-7-3z"/></svg><b>DONATION PAGES</b><p class="m-copy">Lorem ipsum dolor sit amet, consectetur adipiscing elit, sed do eiusmod.</p><i></i></article>
      <article class="m-svc" style="top:314px"><svg viewBox="0 0 20 20" fill="none" stroke="#f5b11e"><rect x="3" y="4" width="12" height="12"/></svg><b>PPC AND FUNNELS</b><p class="m-copy">Lorem ipsum dolor sit amet, consectetur adipiscing elit, sed do eiusmod.</p><i></i></article>
      <article class="m-svc" style="top:398px"><svg viewBox="0 0 20 20" fill="none" stroke="#f5b11e"><rect x="2" y="3" width="16" height="12"/></svg><b>VIDEO MARKETING</b><p class="m-copy">Lorem ipsum dolor sit amet, consectetur adipiscing elit, sed do eiusmod.</p><i></i></article>
      <article class="m-svc" style="top:482px"><svg viewBox="0 0 20 20" fill="none" stroke="#f5b11e"><path d="M3 17h14M5 17v-5M9 17V8M13 17v-7M17 17V5"/></svg><b>ANALYTICS AND OPTIMIZATION</b><p class="m-copy">Lorem ipsum dolor sit amet, consectetur adipiscing elit, sed do eiusmod.</p><i></i></article>
    </section>

    <section class="m-sec m-portfolio">
      <p class="m-eyebrow m-pad">Our Recent Work Done</p>
      <h2 class="m-h2 m-pad">PORTFOLIO</h2>
      <p class="m-copy m-pad">Lorem ipsum dolor sit amet, consectetur adipiscing elit, sed do eiusmod tempor.</p>
      <ul class="m-tabs m-pad"><li>WEBSITES</li><li>LANDING PAGES</li><li>DONATION PAGES</li><li>PPC AND FUNNELS</li><li>VIDEO MARKETING</li></ul>
      <div class="m-shot" role="img" aria-label="Screenshot of a real estate client website"><div>HARBIN REALTY<span>Website Development</span></div></div>
      <div class="m-dots"><span></span><span></span><span></span></div>
      <a class="m-btn">VIEW ALL PROJECTS</a>
    </section>

    <section class="m-sec m-testi">
      <p class="m-eyebrow m-pad">What Our Happy Clients Say</p>
      <h2 class="m-h2 m-pad">TESTIMONIALS</h2>
      <blockquote class="m-quote"><b>”</b><p class="m-copy">Lorem ipsum dolor sit amet, consectetur adipiscing elit, sed do eiusmod tempor incididunt ut labore et dolore magna aliqua. Quis ipsum suspendisse.</p></blockquote>
      <div class="m-author"><i role="img" aria-label="Client portrait"></i><div><b>MAREN HOLT</b><span>Northfield Group</span></div></div>
    </section>

    <section class="m-sec m-cases" role="img" aria-label="Dark photo backdrop of a person working at a desk">
      <p class="m-eyebrow m-pad">How We Work</p>
      <h2 class="m-h2 m-pad">CASE STUDIES</h2>
      <ul class="m-case-list m-pad"><li>Case Study Number One</li><li>Case Study Number Two</li><li>Case Study Number Three</li><li>Case Study Number Four</li><li>Case Study Number Five</li><li>Case Study Number Six</li></ul>
    </section>

    <section class="m-sec m-team">
      <p class="m-eyebrow m-pad">Meet The Members</p>
      <h2 class="m-h2 m-pad">OUR TEAM</h2>
      <div class="m-member" style="top:36px"><div role="img" aria-label="Team member portrait in a yellow shirt"></div><b>MAREN HOLT</b><span>Web Developer</span></div>
      <div class="m-member" style="top:141px"><div role="img" aria-label="Team member portrait in a yellow shirt"></div><b>MAREN HOLT</b><span>Web Developer</span></div>
      <div class="m-member" style="top:246px"><div role="img" aria-label="Team member portrait in a yellow shirt"></div><b>MAREN HOLT</b><span>Web Developer</span></div>
      <div class="m-member" style="top:351px"><div role="img" aria-label="Team member portrait in a yellow shirt"></div><b>MAREN HOLT</b><span>Web Developer</span></div>
    </section>

    <section class="m-sec m-audit">
      <p class="m-eyebrow m-pad">Get In Touch</p>
      <h2 class="m-h2 m-pad">GET A FREE AUDIT<br>AND CONSULTATION</h2>
      <div class="m-audit__pic" role="img" aria-label="Photo of a smiling man in a yellow shirt working on a laptop"></div>
      <form class="m-form">
        <div class="m-field">First Name*</div><div class="m-field">Last Name*</div><div class="m-field">Email Address*</div><div class="m-field">Phone Number*</div><div class="m-field m-field--msg">Message*</div>
        <a class="m-btn">GET FREE CONSULTATION</a>
      </form>
    </section>

    <footer class="m-sec m-footer">
      <div class="m-brand"><b>TALVERN</b><span>STRATEGIES</span></div>
      <p class="m-copy">Lorem ipsum dolor sit amet, consectetur adipiscing elit, sed do eiusmod tempor incididunt ut labore et dolore magna aliqua. Quis ipsum suspendisse ultrices gravida.</p>
      <h4 class="m-ftitle" style="top:100px">QUICK LINKS</h4>
      <ul class="m-flinks" style="top:110px"><li>Home</li><li>What We Do</li><li>Portfolio</li><li>Case Studies</li><li>Contact</li></ul>
      <h4 class="m-ftitle" style="top:180px">CONTACT US</h4>
      <ul class="m-contact"><li><i></i>123456789</li><li><i></i>youremail@example.com</li><li><i></i>4417 Marlow Lane, Fenwick, Ohio</li></ul>
      <p class="m-copyright">Copyright © 2021 <b>Talvern Strategies</b> - All Rights Reserved.</p>
    </footer>
  </main>

</div>
</body>
</html>
```